Football (soccer) board game app design

Hi,

We are a start up looking for a gameplay design for an app. It is a football trivia app that consists of four main screens; login/register, main navigation, gameplay, question.

OVERALL:
We want our app to be kept in a dark theme. Black or very dark gray is preferable, with a couple of nice colors to give it a stylish touch. We like flat designs, but are open for ideas within the general structure design. The logo can be used in the app, but feel free to improve it you feel you can. In the attached material we have tried to outline some of our ideas and other designs friends have helped us make.

LOGIN/REGISTER:
We want a simple login. Email, password, Chatterly login and the possibility to register a new user. Live search check whether the email is valid and free, and there is also live validation of passwords. If this could be incorporated in the design it would be nice.

MAIN NAVIGATION:
In the main navigation screen we want it to be divided into tabs. A home, my games, my categories and a ranking tab. In the top bar it should be possible to search for categories as well as there should be a button to go to settings.

The Home tab
In the home tab we want a "Quick Play" button, and a list of featured categories. A category can be unlocked or locked, which should be illustrated somehow. When a category is tapped it should divide the block into a left and right tap area, where the user can choose to "Beat to unlock" or "Buy to unlock" if locked and "Practice" or "Challenge Friend" if already unlocked.

The My Games tab
In the my games tab, the current games should be divided into three lists. First "your turn", then "opponents turn" and finally "finished games".

The My Categories tab
This tab should include a list of categories, which the user have bought, but as of design it is fairly similar to the blocks in home tab. So not much different here.

The Ranking tab
Ranking should show a set of leaderboards; Today, This Week, This Month, etc. The row in a leaderboard should have teamname and a win percentage.

GAMEPLAY:
The gameplay is inspired by an old football (soccer) board game from the 1950's, and our gameplay consists of three core elements; a football (soccer) pitch, 11 players and a scoreboard.

The football (soccer) pitch
What we need is a pitch seen from behind the goal line. The important issue here, is the perspective, as we want 11 players on the field formed as a 4-3-3 formation, being 1 goalkeeper, 4 defenders, 3 midfielder and 3 strikers. They should all be touchable without overlap. In the other end we want a goal that should be touchable as well. The goal in the nearest end do not have to be visible. Due to the perspective of the field and the fact that players and goal should be touchable, of course give you the opportunity to play around with the proportions of both players and goal. We rather want a large goal being out of proportions, than a small goal with a tiny tap area. Around the field (sidelines and beside the goal) we would like advertising banners like seen on a real stadium.

The players
As mentioned we want 11 players in a 4-3-3 formation. The players should be attached to the board with springs as seen on some of the very old board games, where you could flick the player to pass the ball. This also means that we want the players to be placed in an indentation for the ball to fall into and it would be very cool if you could illustrate the player with the ball, as being pulled back to one of the sides, just enough to see the ball at his feet. The players should be large enough for a user to tap them, hence it would also be beneficial if they are not overlapping. For a start we would like to see the players in a blue shirt and white shorts (socks are not necessary as they are placed on a spring).

Scoreboard
On the scoreboard above the field, we need information such as the names of the two teams (could be FC Brightmoor and Tall Oak Rovers), the score (2-1), minutes played (42), and which half (1st). We also want a progress bar that illustrates how many moves you have used ranging from 0-5. The scoreboard could be inspired from the ones seen around stadiums across the world, but feel free to improvise.

What We Are Looking for
We are looking for full PSD and AI files so we can use them to make minor changes like colors on shirts and shorts, colors on pitch, etc. We really want you to be innovative and inspire us, as we are not designers ourselves. In the attached files, we have tried to sketch out a design that covers our initial ideas. We are looking for a professional look, and having the players and field look like a real board game would just be awesome. A combination of the look from the realistic pitch with advertising banners around it, the idea of our spring-players and the initial thoughts of a design illustrated in our sketch, should help you along. Flat design, cartoonish or somewhere in between is up to you, we just want you to impress and make "wow"-feeling.

QUESTION:
The final screen should display a question with four possible answers. There should be a green/checkmark when correct answer, and a red/cross if incorrect.

That's all. We are looking very much forward to see your designs!
Updates

Hi all,

We have changed the terms of the contest to now have a guaranteed payment, and we are really looking forward to see your designs! Good luck.

/ Mikkel and Anders

By request we have now uploaded an AI-file with the logo for you to play around with. We are looking forward to see your designs.

/ Mikkel and Anders

Reason: Hi designers, We are really happy with the progress being made, and are looking forward to see some of the designs that are still work in progress. However the amount of designs received, has not reached our expectations yet. Therefore we are extending the deadline for seven more days, so designers, that are still working on their designs can continue their work without a stressing deadline in the horizon. Good luck to all of you. We are looking very much forward to see, what you are able to produce. Best regards, Mikkel and Anders

Reason: Hi all, We still have a lot of designers in the competition , who are battling to finish their designs, therefore we have decided to extend the deadline once more. Good luck to all of you!

Target Market(s)

Football (soccer) fans

Industry/Entity Type

Advertising

```html
<!DOCTYPE html>
<html lang="en">
<head>
<meta charset="utf-8">
<title>Matches</title>
<link rel="stylesheet" href="https://fonts.googleapis.com/css2?family=Oswald:wght@500;600&family=PT+Sans+Narrow:wght@400;700&family=PT+Sans:wght@700&display=swap">
<style>
  :root{
    --bg:#17212a;
    --bg-deep:#121a21;
    --nav:#1b252e;
    --nav-active:#222d37;
    --panel:#1f2a33;
    --row:#4a5058;
    --minute:#4f555d;
    --score:#898e94;
    --score-text:#1e2830;
    --blue:#0aa3e8;
    --white:#ffffff;
    --muted:#a6abb0;
    --red:#e84c4c;
    --line:#6a7077;
  }
  *{box-sizing:border-box;margin:0;padding:0}
  html,body{width:676px;height:1200px;overflow:hidden}
  body{background:linear-gradient(180deg,var(--bg) 0%,var(--bg-deep) 100%);font-family:"PT Sans",sans-serif;color:var(--white);position:relative}

  .tabs{position:absolute;left:0;top:0;width:676px;height:99px;display:flex;background:var(--nav)}
  .tab{flex:1;display:flex;align-items:center;justify-content:center;font-family:"PT Sans Narrow",sans-serif;font-size:23px;letter-spacing:4px;color:#d6dadd;border-right:1px solid #131b22;position:relative}
  .tab:last-child{border-right:0}
  .tab.active{background:var(--nav-active)}
  .tab.active::before{content:"";position:absolute;left:0;right:0;top:0;height:6px;background:var(--blue)}

  .stats{position:absolute;left:17px;top:116px;width:644px;height:190px;background:var(--panel)}
  .stat{position:absolute;top:20px;font-family:"Oswald",sans-serif;font-weight:600;font-size:100px;line-height:1;letter-spacing:-2px}
  .stat.won{left:38px;color:var(--blue)}
  .stat.pct{right:34px;color:var(--white)}
  .stat-label{position:absolute;top:124px;font-size:32px;font-weight:700}
  .stat-label.won{left:41px}
  .stat-label.pct{right:36px}

  .period{position:absolute;left:17px;top:313px;width:644px;height:52px;border:1px solid #3a444d;display:flex}
  .period .arrow{width:152px;display:flex;align-items:center;justify-content:center}
  .period .current{flex:1;background:#474d55;display:flex;align-items:center;justify-content:center;font-family:"PT Sans Narrow",sans-serif;font-size:23px;letter-spacing:5px;color:#dfe2e5}

  .band{position:absolute;left:21px;width:640px;height:69px;display:flex;align-items:center;justify-content:center;font-family:"PT Sans Narrow",sans-serif;font-size:27px;letter-spacing:6px}
  .band.your{top:408px;background:var(--blue);color:var(--white)}
  .band.opponent{top:754px;background:var(--white);color:#1d2730}
  .band.finished{top:1101px;background:var(--bg-deep);border:1px solid #e6e9ec;color:var(--white)}

  .match{position:absolute;left:27px;width:628px;height:128px;display:flex;background:var(--row)}
  .minute{width:104px;background:var(--minute);display:flex;align-items:center;justify-content:center;font-family:"Oswald",sans-serif;font-weight:500;font-size:54px;color:#b0b4b8;letter-spacing:-2px}
  .scores{width:64px;display:flex;flex-direction:column}
  .scores span{flex:1;background:var(--score);display:flex;align-items:center;justify-content:center;font-size:29px;font-weight:700;color:var(--score-text)}
  .scores span:first-child{border-bottom:2px solid var(--row)}
  .teams{flex:1;display:flex;flex-direction:column;border-left:1px solid #3d434a}
  .teams span{flex:1;display:flex;align-items:center;padding-left:19px;font-size:30px;font-weight:700;color:#f2f4f5}
  .teams span:first-child{border-bottom:2px solid #3f454c}
  .card{display:inline-block;width:22px;height:27px;background:var(--red);margin-left:16px}
  .chevron{position:absolute;right:16px;top:50%;margin-top:-17px}
</style>
</head>
<body>
  <nav class="tabs">
    <div class="tab">HOME</div>
    <div class="tab active">MATCHES</div>
    <div class="tab">RANKINGS</div>
    <div class="tab">SETTINGS</div>
  </nav>

  <section class="stats">
    <div class="stat won">127</div>
    <div class="stat-label won">Matches Won</div>
    <div class="stat pct">58%</div>
    <div class="stat-label pct">Winning Percentage</div>
  </section>

  <div class="period">
    <div class="arrow"><svg width="14" height="24" viewBox="0 0 14 24"><path d="M12 2 2 12l10 10" fill="none" stroke="#cfd3d6" stroke-width="2"/></svg></div>
    <div class="current">THIS WEEK</div>
    <div class="arrow"><svg width="14" height="24" viewBox="0 0 14 24"><path d="m2 2 10 10L2 22" fill="none" stroke="#cfd3d6" stroke-width="2"/></svg></div>
  </div>

  <div class="band your">YOUR TURN</div>

  <div class="match" style="top:478px">
    <div class="minute">42’</div>
    <div class="scores"><span>2</span><span>0</span></div>
    <div class="teams"><span>Tall Oak Rovers<i class="card"></i></span><span>FC Brightmoor</span></div>
    <svg class="chevron" width="18" height="34" viewBox="0 0 18 34"><path d="m2 2 14 15L2 32" fill="none" stroke="#c3c7cb" stroke-width="2"/></svg>
  </div>
  <div class="match" style="top:609px">
    <div class="minute">90’</div>
    <div class="scores"><span>2</span><span>4</span></div>
    <div class="teams"><span>Tall Oak Rovers</span><span>FC Brightmoor</span></div>
    <svg class="chevron" width="18" height="34" viewBox="0 0 18 34"><path d="m2 2 14 15L2 32" fill="none" stroke="#c3c7cb" stroke-width="2"/></svg>
  </div>

  <div class="band opponent">OPPONENTS TURN</div>

  <div class="match" style="top:825px">
    <div class="minute">8’</div>
    <div class="scores"><span>2</span><span>0</span></div>
    <div class="teams"><span>Tall Oak Rovers</span><span>FC Brightmoor</span></div>
    <svg class="chevron" width="18" height="34" viewBox="0 0 18 34"><path d="m2 2 14 15L2 32" fill="none" stroke="#c3c7cb" stroke-width="2"/></svg>
  </div>
  <div class="match" style="top:956px">
    <div class="minute">17’</div>
    <div class="scores"><span>2</span><span>0</span></div>
    <div class="teams"><span>Tall Oak Rovers</span><span>FC Brightmoor</span></div>
    <svg class="chevron" width="18" height="34" viewBox="0 0 18 34"><path d="m2 2 14 15L2 32" fill="none" stroke="#c3c7cb" stroke-width="2"/></svg>
  </div>

  <div class="band finished">FINISHED MATCHES</div>

  <div class="match" style="top:1171px">
    <div class="minute"></div>
    <div class="scores"><span style="align-items:flex-start;padding-top:12px">2</span><span>0</span></div>
    <div class="teams"><span style="align-items:flex-start;padding-top:10px">Tall Oak Rovers</span><span>FC Brightmoor</span></div>
  </div>
</body>
</html>
```